Design a brand style for my candle

Hi!
We need a label design created to start off our candle company, we look to create a fun, girly, cool and on trend brand. We are wanting a label to go on candles with a quote on it "Love yo'self". Please use this quote when submitting your design, if you could place it on a candle that would be awesome. We love the pastel colours of pink, how this is incorporated in other colours we look forward to your designs. I have attached photos as a start of a "mood board" . The font and style must be easily changed to suit other quotes and sayings
Thanks so much!
Updates

Looking for something modern, minimalist, cool and on Trend packaging targeting 20's women Added Thursday, January 5, 2017

Target Market(s)

Women 20-35
Style - Fun, Flirty, Clean Lines and Cool

Industry/Entity Type

Retail

Font styles to use
Sans Serif

Requirements
Must have
• pastel pink, the quote "Love yo'self" on the candle (pic is an example only, please do not use the same font)

```html
<!DOCTYPE html>
<html lang="en">
<head>
<meta charset="utf-8">
<title>Candle Labels</title>
<link rel="stylesheet" href="https://fonts.googleapis.com/css2?family=Roboto+Slab:wght@500&family=Open+Sans:wght@400&display=swap">
<style>
  :root {
    --page-bg: #ffffff;
    --label-fill: #fdc9c9;
    --ring-pink: #fa9797;
    --ring-blue: #7fb9ec;
    --quote-white: #ffffff;
    --name-red: #c23a32;
    --name-blue: #3d90e0;
    --divider: #fbe9e9;
  }
  html, body {
    margin: 0;
    padding: 0;
    width: 1200px;
    height: 826px;
    overflow: hidden;
    background: var(--page-bg);
  }
  .label-sheet {
    display: block;
    width: 1200px;
    height: 826px;
  }
  .label-face { fill: var(--label-fill); }
  .label-ring { fill: none; stroke-width: 13; }
  .label-ring--pink { stroke: var(--ring-pink); }
  .label-ring--blue { stroke: var(--ring-blue); }
  .quote {
    font-family: "Roboto Slab", sans-serif;
    font-weight: 500;
    fill: var(--quote-white);
    text-anchor: middle;
  }
  .quote--large { font-size: 64px; letter-spacing: -1px; }
  .quote--medium { font-size: 57px; letter-spacing: -1px; }
  .divider-line { stroke: var(--divider); stroke-width: 1; }
  .divider-mark { fill: var(--divider); }
  .company-name {
    font-family: "Open Sans", sans-serif;
    font-size: 11.5px;
    text-anchor: middle;
    letter-spacing: 0.2px;
  }
  .company-name--red { fill: var(--name-red); }
  .company-name--blue { fill: var(--name-blue); }
</style>
</head>
<body>
<svg class="label-sheet" viewBox="0 0 1200 826" xmlns="http://www.w3.org/2000/svg">
  <g class="candle-label candle-label--love">
    <circle class="label-face" cx="324" cy="476" r="160"/>
    <circle class="label-ring label-ring--pink" cx="324" cy="476" r="153.5"/>
    <text class="quote quote--large" x="324" y="440">LOVE</text>
    <text class="quote quote--large" x="324" y="520">YO’SELF</text>
    <line class="divider-line" x1="240" y1="554" x2="408" y2="554"/>
    <rect class="divider-mark" x="320" y="550" width="8" height="8" transform="rotate(45 324 554)"/>
    <text class="company-name company-name--red" x="324" y="581">COMPANY NAME</text>
  </g>
  <g class="candle-label candle-label--woke">
    <circle class="label-face" cx="875" cy="476" r="160"/>
    <circle class="label-ring label-ring--blue" cx="875" cy="476" r="153.5"/>
    <text class="quote quote--medium" x="875" y="431">I WOKE</text>
    <text class="quote quote--medium" x="875" y="491">UP LIKE</text>
    <text class="quote quote--medium" x="875" y="551">THIS</text>
    <line class="divider-line" x1="791" y1="572" x2="959" y2="572"/>
    <rect class="divider-mark" x="871" y="568" width="8" height="8" transform="rotate(45 875 572)"/>
    <text class="company-name company-name--blue" x="875" y="601">COMPANY NAME</text>
  </g>
</svg>
</body>
</html>
```